Door Sticker for Loyalty Rewards App

We need to make stickers that will go on the door of the merchants who are part of the Quiver app.

I have attached the Quiver logo, our colours and examples of other door stickers.

Target Market(s)

Millennials

Colors

Designer to choose colors to be used in the design.

Requirements
Must have
• We would like the Quiver logo as the biggest part of the sticker with the text "Effortless Rewards Available Here" and our URL: www.TrulyQuiverTime.com (you can drop the www if you want).
• Must use the Quiver colours.

```html
<!DOCTYPE html>
<html lang="en">
<head>
<meta charset="utf-8">
<title>Quiver Door Sticker</title>
<link rel="stylesheet" href="https://fonts.googleapis.com/css2?family=Jost:wght@600;700&display=swap">
<style>
  :root {
    --backdrop: #e6e8ec;
    --quiver-pink: #f0559f;
    --quiver-blue: #3aa3e3;
    --quiver-violet: #8a72d6;
    --ink-navy: #2b2a5e;
    --tagline-blue: #3a9ee0;
    --paper: #ffffff;
  }
  * { margin: 0; padding: 0; box-sizing: border-box; }
  html, body {
    width: 1200px;
    height: 901px;
    overflow: hidden;
    background: var(--backdrop);
    font-family: "Jost", sans-serif;
  }
  .canvas {
    position: relative;
    width: 1200px;
    height: 901px;
  }
  .sticker {
    position: absolute;
    left: 426px;
    top: 171px;
    width: 380px;
    height: 555px;
    border-radius: 18px 170px 170px 18px;
    background: linear-gradient(35deg, var(--quiver-pink) 0%, var(--quiver-pink) 30%, var(--quiver-violet) 58%, var(--quiver-blue) 85%);
  }
  .sticker-face {
    position: absolute;
    inset: 28px 30px 30px 26px;
    border-radius: 6px 145px 145px 6px;
    background: var(--paper);
  }
  .brand-square {
    position: absolute;
    left: 61px;
    top: 58px;
    width: 184px;
    height: 184px;
    background: var(--quiver-pink);
  }
  .brand-name {
    position: absolute;
    left: 58px;
    top: 308px;
    font-size: 50px;
    font-weight: 700;
    line-height: 1;
    color: var(--ink-navy);
    letter-spacing: 0.5px;
  }
  .tagline {
    position: absolute;
    left: 58px;
    top: 372px;
    width: 206px;
    text-align: center;
    font-size: 22px;
    font-weight: 700;
    line-height: 1.5;
    color: var(--tagline-blue);
  }
  .url-pill {
    position: absolute;
    left: 26px;
    top: 438px;
    width: 226px;
    height: 40px;
    border-radius: 0 20px 20px 0;
    background: linear-gradient(90deg, var(--quiver-pink) 0%, #ec5aa9 70%, #d86cc4 100%);
    color: var(--paper);
    font-size: 18px;
    font-weight: 700;
    line-height: 40px;
    padding-left: 14px;
    white-space: nowrap;
  }
</style>
</head>
<body>
  <main class="canvas">
    <div class="sticker">
      <div class="sticker-face"></div>
      <div class="brand-square"></div>
      <div class="brand-name">Quiver</div>
      <p class="tagline">Effortless Rewards<br>Available Here</p>
      <div class="url-pill">TrulyQuiverTime.com</div>
    </div>
  </main>
</body>
</html>
```